Book Cover For Social Media Project

I am requiring a book cover for my upcoming book “Folding Waves Toward Harvests”

This book is for Network Marketers wanting to build their business on Social Media. Helping them get business from likes they receive on Chatterloom.

The book design needs to be clear that it is a business book that is all about social media is a fun, modern way.

Target Market(s)

Men and Women aged 18-65 wanting to make money from their social media accounts.

Industry/Entity Type

Business

Colors

Designer to choose colors to be used in the design.

Requirements
Must have
• Clear and obvious relationship to social media and business.
• The title “Folding Waves Toward Harvests”
• Author name “Dorian Halvette”
• Tag line “A Complete Handbook For Growing Your Direct Selling Venture Through Online Channels”
Nice to have
• Emojis that are used on Chatterloom.

```html
<!DOCTYPE html>
<html lang="en">
<head>
<meta charset="utf-8">
<title>Folding Waves Toward Harvests — Book Cover</title>
<link rel="stylesheet" href="https://fonts.googleapis.com/css2?family=Oswald:wght@600;700&family=Arimo:wght@700&display=swap">
<style>
  :root {
    --backdrop: #e4e4e6;
    --cover-white: #ffffff;
    --cover-blue: #30508f;
    --frame-blue: #2d4d93;
    --title-red: #c4161c;
    --title-blue: #2f53a3;
    --title-black: #111111;
    --figure-white: #f2f4f8;
    --crowd-tone: #1f3567;
  }
  html, body {
    margin: 0;
    padding: 0;
    width: 1200px;
    height: 1200px;
    overflow: hidden;
    background: var(--backdrop);
  }
  .canvas {
    position: relative;
    width: 1200px;
    height: 1200px;
  }
  .cover {
    position: absolute;
    left: 200px;
    top: 80px;
    width: 800px;
    height: 1040px;
    background: var(--cover-white);
    overflow: hidden;
    box-shadow: 0 18px 40px rgba(0,0,0,0.18);
  }
  .cover__lower-band {
    position: absolute;
    left: 0;
    top: 420px;
    width: 800px;
    height: 620px;
    background: var(--cover-blue);
  }
  .crowd-slot {
    position: absolute;
    left: 600px;
    top: 378px;
    width: 170px;
    height: 42px;
    background: var(--crowd-tone);
    border-radius: 21px 21px 0 0;
  }
  .figure-slot {
    position: absolute;
    left: 300px;
    top: 540px;
    width: 150px;
    height: 430px;
    background: var(--figure-white);
    border-radius: 40px 40px 6px 6px;
  }
  .chat-bubble {
    position: absolute;
    left: 100px;
    top: 140px;
    width: 560px;
    height: 450px;
    filter: drop-shadow(0 6px 8px rgba(0,0,0,0.2));
  }
  .chat-bubble__shape {
    fill: var(--cover-white);
    stroke: var(--frame-blue);
    stroke-width: 16;
    stroke-linejoin: round;
  }
  .title {
    position: absolute;
    left: 108px;
    top: 148px;
    width: 544px;
    height: 380px;
    margin: 0;
    display: flex;
    flex-direction: column;
    align-items: center;
    justify-content: center;
    font-family: "Oswald", "Arial Narrow", sans-serif;
    font-weight: 700;
    text-transform: uppercase;
    line-height: 0.95;
  }
  .title__lead { color: var(--title-red); font-size: 74px; letter-spacing: 1px; }
  .title__main { color: var(--title-blue); font-size: 150px; letter-spacing: 2px; }
  .title__tail { color: var(--title-black); font-size: 56px; letter-spacing: 1px; }
  .tagline {
    position: absolute;
    left: 480px;
    top: 620px;
    width: 290px;
    margin: 0;
    color: var(--cover-white);
    font-family: "Arimo", Arial, sans-serif;
    font-weight: 700;
    font-size: 28px;
    line-height: 1.12;
  }
  .author {
    position: absolute;
    right: 40px;
    top: 900px;
    margin: 0;
    color: var(--cover-white);
    font-family: "Arimo", Arial, sans-serif;
    font-weight: 700;
    font-size: 24px;
  }
</style>
</head>
<body>
  <main class="canvas">
    <section class="cover">
      <div class="cover__lower-band"></div>
      <div class="crowd-slot" role="img" aria-label="Small silhouettes of a cheering crowd"></div>
      <div class="figure-slot" role="img" aria-label="White silhouette of a businessman holding the title bubble above his head"></div>
      <svg class="chat-bubble" viewBox="0 0 560 450" aria-hidden="true">
        <path class="chat-bubble__shape" d="M52 8 H508 A44 44 0 0 1 552 52 V344 A44 44 0 0 1 508 388 H180 L90 442 L112 388 H52 A44 44 0 0 1 8 344 V52 A44 44 0 0 1 52 8 Z"/>
      </svg>
      <h1 class="title">
        <span class="title__lead">Folding</span>
        <span class="title__main">Waves</span>
        <span class="title__tail">Toward Harvests</span>
      </h1>
      <p class="tagline">A Complete Handbook For Growing Your Direct Selling Venture Through Online Channels</p>
      <p class="author">Dorian Halvette</p>
    </section>
  </main>
</body>
</html>
```